Dubai Family protection infographic

We need to produce a way of attracting people to a life insurance and critical illness cover seminar. As this is a pretty dull subject for most people, so we need a cool way of getting people to read the invite/marketing collateral.

We're thinking some kind of colourful and attractive infographic that we can use on flyers and posters as well as online and as an emailer.

Content for the graphic is as bellow:

How much does it cost to replace Mum & Dad?

Mum = Chauffer, Cook, Laundry Service, Household Cleaner, Psychologist, Money Manager

Mums typically work a 94-hour week. At a rather paltry $12 per hour, that’s $4,888 per month – or $58,656 each year. (Source: paywell.net)

Dad : The average Western Expat’s salary in the Gulf is $12,215 per month. That’s $146,580 each year. (Source: Harbor Ledger).

Did you know that the average age of critical illness claimants in the Middle East last year was just 48. Of these, 44% were for cancer while 41% were heart related.

The average age of a death claimant was just 50 years old.
(Source: Lindqvist Mutual Assurance)

1 in 3 people will develop some form of cancer during their lifetime.

That’s 2.36 billion people globally.

And that’s equivalent to the population of China, USA, Brazil, Russia, Philippines, France, UK, South Africa and Italy combined.

Does your family have the resources to hand to cope if a tragedy happens to you?

What can you do to protect them and yourself?

Come to the UAE’s first national protection seminar to find out. Join us at Palmcrest Memorial Sports Ground on June 19th at 19:00.

To pre-register, visit www.brightvane.com/events or alternatively register on the door.

```html
<!DOCTYPE html>
<html lang="en">
<head>
<meta charset="utf-8">
<title>How much does it cost to replace Mum &amp; Dad?</title>
<link href="https://fonts.googleapis.com/css2?family=Nunito:wght@400;600;800;900&display=swap" rel="stylesheet">
<style>
:root{
  --plum:#47333f;
  --rose:#e8607a;
  --sand:#b6ad9b;
  --paper:#efefef;
  --page:#ffffff;
  --ink:#47333f;
  --rule:#c9c2b6;
}
*{margin:0;padding:0;box-sizing:border-box}
html,body{width:1200px;height:1000px;overflow:hidden;background:var(--page)}
body{font-family:"Nunito",sans-serif;color:var(--ink);position:relative}
.infographic{position:absolute;left:333px;top:0;width:534px;height:997px;background:var(--paper);overflow:hidden}
.abs{position:absolute}
.header{left:0;top:0;width:534px;height:85px;background:var(--plum);color:#fff;padding:12px 20px;font-weight:900;font-size:29px;line-height:31px;letter-spacing:.2px}
.section-title{font-weight:900;font-size:21px}
.mum-title{left:20px;top:96px;color:var(--rose)}
.figure{background:var(--rose);border-radius:20px 20px 4px 4px}
.equals{left:102px;top:164px;color:var(--rose);font-size:34px;font-weight:800}
.role{display:flex;align-items:center;gap:10px;font-size:17px;white-space:nowrap}
.role svg{width:28px;height:28px;flex:none}
.rule-rose{left:157px;top:241px;width:357px;height:1px;background:var(--rose)}
.lead{left:157px;top:256px;width:360px;font-size:13px;line-height:15.5px}
.stat-label{font-weight:900;font-size:15px}
.chevron{width:22px;height:24px}
.rule-grey{left:20px;top:387px;width:494px;height:1px;background:var(--rule)}
.dad-title{left:20px;top:400px}
.circle-icon{width:30px;height:30px;border-radius:50%;background:var(--sand);display:flex;align-items:center;justify-content:center}
.body-text{font-size:13px;line-height:15.5px}
.body-text b{font-weight:900}
.divider{left:141px;top:404px;width:1px;height:354px;background:var(--sand)}
.fact{left:157px;width:152px}
.band{left:0;width:534px;color:#fff}
.band p{position:absolute;left:142px;font-size:13px;line-height:16px;font-weight:800}
.band-question{top:772px;height:73px;background:var(--plum)}
.band-venue{top:845px;height:68px;background:var(--rose)}
.band-web{top:913px;height:57px;background:var(--sand)}
.band-sources{top:970px;height:27px;background:var(--plum)}
.sources{left:142px;top:7px;font-size:11px;line-height:13px;font-weight:600;white-space:nowrap}
.sources span{margin-right:16px}
.placeholder{border-radius:6px}
</style>
</head>
<body>
<main class="infographic">
  <h1 class="abs header">How much does it cost to replace<br>Mum &amp; Dad?</h1>

  <h2 class="abs section-title mum-title">Mum</h2>
  <div class="abs figure" style="left:22px;top:134px;width:46px;height:96px" role="img" aria-label="Pink silhouette of a mother"></div>
  <div class="abs equals">=</div>

  <div class="abs role" style="left:157px;top:134px">
    <svg viewBox="0 0 28 28" fill="none" stroke="#47333f" stroke-width="1.6"><path d="M5 16c-3-1-3-7 1-8 0-4 6-5 8-3 3-2 8 0 8 4 4 1 3 7 0 8-1 3-5 3-7 2l-2 5h-3l1-5c-3 1-5 0-6-3z"/></svg>
    <span>Psychologist</span></div>
  <div class="abs role" style="left:157px;top:169px">
    <svg viewBox="0 0 28 28" fill="none" stroke="#47333f" stroke-width="1.6"><path d="M7 16c-4 0-5-7 0-8 1-4 8-5 10-2 4-2 9 2 6 7l-2 3z"/><path d="M8 16v7h13v-7"/></svg>
    <span>Cook</span></div>
  <div class="abs role" style="left:157px;top:203px">
    <svg viewBox="0 0 28 28" fill="none" stroke="#47333f" stroke-width="2"><circle cx="14" cy="14" r="11"/><circle cx="14" cy="15" r="3"/><path d="M4 13h7M17 13h7M14 18v6"/></svg>
    <span>Chauffeur</span></div>
  <div class="abs role" style="left:330px;top:134px">
    <svg viewBox="0 0 28 28" fill="none" stroke="#47333f" stroke-width="1.6"><rect x="5" y="2" width="18" height="24" rx="1"/><path d="M5 7h18"/><circle cx="14" cy="16" r="6"/></svg>
    <span>Laundry Service</span></div>
  <div class="abs role" style="left:330px;top:169px">
    <svg viewBox="0 0 28 28"><path fill="#47333f" d="M10 3h8l-2 5c6 2 9 8 8 13-1 4-5 5-10 5s-9-1-10-5c-1-5 2-11 8-13z"/><text x="14" y="22" fill="#fff" font-size="11" font-weight="800" text-anchor="middle" font-family="Nunito,sans-serif">$</text></svg>
    <span>Money Manager</span></div>
  <div class="abs role" style="left:330px;top:203px">
    <svg viewBox="0 0 28 28" fill="none" stroke="#47333f" stroke-width="1.6"><path d="M16 3l-6 18"/><path d="M6 21h8l1 4H5z"/><circle cx="21" cy="23" r="3"/></svg>
    <span>Houshold Cleaner</span></div>

  <div class="abs rule-rose"></div>
  <p class="abs lead">Mums typically work a 94-hour week. At a rather paltry $12 per hour, that’s $4,888 per month – or $58,656 each year.</p>

  <div class="abs stat-label" style="left:165px;top:306px">x94</div>
  <svg class="abs" style="left:158px;top:330px" width="44" height="44" viewBox="0 0 44 44"><circle cx="22" cy="22" r="20" fill="none" stroke="#e8607a" stroke-width="2.5"/><path d="M22 22V6a16 16 0 0 1 13 6z" fill="#e8607a"/></svg>
  <svg class="abs chevron" style="left:245px;top:342px" viewBox="0 0 22 24"><path d="M2 0h9l10 12-10 12H2l10-12z" fill="#47333f"/></svg>
  <div class="abs stat-label" style="left:300px;top:306px">$4,888</div>
  <svg class="abs" style="left:310px;top:330px" width="44" height="38" viewBox="0 0 44 38"><rect x="1" y="3" width="42" height="34" rx="2" fill="#e8607a"/><g fill="#fff"><rect x="6" y="13" width="5" height="4"/><rect x="14" y="13" width="5" height="4"/><rect x="22" y="13" width="5" height="4"/><rect x="30" y="13" width="5" height="4"/><rect x="6" y="20" width="5" height="4"/><rect x="14" y="20" width="5" height="4"/><rect x="22" y="20" width="5" height="4"/><rect x="30" y="20" width="5" height="4"/><rect x="6" y="27" width="5" height="4"/><rect x="14" y="27" width="5" height="4"/><rect x="22" y="27" width="5" height="4"/></g></svg>
  <svg class="abs chevron" style="left:394px;top:342px" viewBox="0 0 22 24"><path d="M2 0h9l10 12-10 12H2l10-12z" fill="#47333f"/></svg>
  <div class="abs stat-label" style="left:450px;top:306px">$58,656</div>
  <svg class="abs" style="left:452px;top:330px" width="62" height="40" viewBox="0 0 62 40" fill="#e8607a"><rect x="0" y="0" width="14" height="12"/><rect x="16" y="0" width="14" height="12"/><rect x="32" y="0" width="14" height="12"/><rect x="48" y="0" width="14" height="12"/><rect x="0" y="14" width="14" height="12"/><rect x="16" y="14" width="14" height="12"/><rect x="32" y="14" width="14" height="12"/><rect x="48" y="14" width="14" height="12"/><rect x="0" y="28" width="14" height="12"/><rect x="16" y="28" width="14" height="12"/><rect x="32" y="28" width="14" height="12"/><rect x="48" y="28" width="14" height="12"/></svg>

  <div class="abs rule-grey"></div>

  <h2 class="abs section-title dad-title">Dad</h2>
  <div class="abs figure" style="left:20px;top:437px;width:34px;height:95px;background:var(--plum);border-radius:16px 16px 3px 3px" role="img" aria-label="Dark silhouette of a father in a suit"></div>
  <div class="abs circle-icon" style="left:94px;top:502px"><svg width="16" height="16" viewBox="0 0 16 16"><path d="M14 2L3 13M3 6v7h7" stroke="#fff" stroke-width="2.4" fill="none"/></svg></div>
  <p class="abs body-text" style="left:22px;top:549px;width:112px">The average Western Expat’s salary in the Gulf is $12,215 per month. That’s $146,580 each year.</p>

  <div class="abs divider"></div>

  <h2 class="abs section-title" style="left:157px;top:400px">Did you know</h2>
  <p class="abs body-text fact" style="top:434px">That the average age of critical illness claimants in the Middle East last year was just <b>48</b>.</p>
  <p class="abs body-text fact" style="top:507px">The average age of a death claimant was just <b>50</b> years old.</p>
  <p class="abs body-text fact" style="top:565px"><b>1</b> in <b>3</b> people will develop some form of cancer during their lifetime.</p>
  <p class="abs body-text fact" style="top:627px">That’s <b>2.36 billion</b> people globally.</p>
  <p class="abs body-text fact" style="top:674px">And that’s equivalent to the population of China, USA, Brazil, Russia, Philippines, France, UK, South Africa and Italy combined.</p>

  <div class="abs circle-icon" style="left:318px;top:458px"><svg width="16" height="16" viewBox="0 0 16 16"><path d="M1 8h13M8 2l6 6-6 6" stroke="#fff" stroke-width="2.4" fill="none"/></svg></div>
  <p class="abs body-text" style="left:362px;top:434px;width:100px">Of these, <b style="font-size:16px">44%</b> were for <b>cancer</b></p>
  <div class="abs placeholder" style="left:464px;top:432px;width:50px;height:62px;background:radial-gradient(circle,#f3b3c0,transparent 70%)" role="img" aria-label="Network of connected dots representing cancer cells"></div>
  <div class="abs placeholder" style="left:360px;top:475px;width:40px;height:70px;background:var(--rose);border-radius:50% 50% 45% 45%" role="img" aria-label="Illustration of a human heart"></div>
  <p class="abs body-text" style="left:402px;top:507px;width:112px">while <b style="font-size:16px">41%</b> were <b>heart</b> related.</p>
  <div class="abs placeholder" style="left:364px;top:560px;width:66px;height:50px;background:linear-gradient(90deg,var(--plum) 0 33%,var(--sand) 33% 100%)" role="img" aria-label="Three person figures, one of three highlighted"></div>
  <div class="abs placeholder" style="left:320px;top:640px;width:198px;height:112px;background:linear-gradient(135deg,var(--sand),#8f7d87)" role="img" aria-label="World map highlighting China, USA, Brazil, Russia, Philippines, France, UK, South Africa and Italy"></div>

  <section class="abs band band-question">
    <svg class="abs" style="left:55px;top:18px" width="38" height="38" viewBox="0 0 38 38"><circle cx="19" cy="19" r="19" fill="#fff"/><text x="19" y="27" text-anchor="middle" font-family="Nunito,sans-serif" font-weight="900" font-size="23" fill="#47333f">?</text></svg>
    <p style="top:15px;width:375px">Does your family have the resources to hand to cope if a tragedy happens to you? What can you do to protect them and yourself?</p>
  </section>
  <section class="abs band band-venue">
    <svg class="abs" style="left:61px;top:13px" width="26" height="38" viewBox="0 0 26 38"><path d="M13 0a13 13 0 0 1 13 13c0 10-13 25-13 25S0 23 0 13A13 13 0 0 1 13 0z" fill="#fff"/><circle cx="13" cy="13" r="5" fill="#e8607a"/></svg>
    <p style="top:13px;width:375px;font-weight:600">Come to the UAE’s first national protection seminar to find out. Join us at <b style="font-weight:900">Palmcrest Memorial Sports Ground on June 19th at 19:00</b></p>
  </section>
  <section class="abs band band-web">
    <div class="abs" style="left:44px;top:14px;font-size:20px;font-weight:900">www</div>
    <p style="top:12px;width:380px;font-size:14px;font-weight:600">To pre-register, visit <b style="font-weight:900">www.brightvane.com/events</b><br>or alternatively register on the door.</p>
  </section>
  <footer class="abs band band-sources">
    <div class="abs sources"><span>Sources:</span>paywell.net | Harbor Ledger | Lindqvist Mutual Assurance</div>
  </footer>
</main>
</body>
</html>
```